Online trading school - Website design

We are building an online trading school (trading of shares, commodities, indices, currencies). The purpose is to teach online traders how to trade successfully. We need to design the homepage of the website and logo (bramwelloq.com will be the domain). The homepage will contain the following elements

- logo
- Sign in and Register links/buttons
- upper menu
- short introduction
- a couple of bullet points 'Why to join our school?'
- sign up form
- text
- bottom menu

Attached is a draft for the designer. The draft is just for an inspiration, the actual structure of the website can be different if the designer thinks so.

The designer is free to choose colors.

School

3 page

```html
<!DOCTYPE html>
<html lang="en">
<head>
<meta charset="utf-8">
<title>bramwelloq – Online Trading School</title>
<link href="https://fonts.googleapis.com/css2?family=Ubuntu:wght@400;500;700&family=Oswald:wght@400;500&display=swap" rel="stylesheet">
<style>
  :root {
    --navy: #1a2340;
    --blue: #4285f4;
    --orange: #e4610a;
    --white: #ffffff;
    --field: #f3f3f4;
    --field-line: #dcdde0;
    --ink: #1d2440;
    --grey-text: #777a80;
    --ring: #c9cacc;
    --label: #8a8c90;
  }
  * { box-sizing: border-box; margin: 0; padding: 0; }
  html, body { width: 1093px; height: 1200px; overflow: hidden; }
  body { font-family: "Ubuntu", sans-serif; color: var(--ink); background: var(--white); position: relative; }

  .site-header { position: absolute; left: 0; top: 0; width: 1093px; height: 72px; background: var(--navy); }
  .brand { position: absolute; left: 82px; top: 19px; display: flex; align-items: center; gap: 10px; }
  .brand-dot { width: 32px; height: 32px; border-radius: 50%; background: var(--orange); }
  .brand-name { font-size: 24px; font-weight: 500; color: var(--white); letter-spacing: -0.3px; }
  .account-links { position: absolute; right: 79px; top: 24px; display: flex; gap: 8px; }
  .account-links a { display: block; border: 1px solid var(--white); color: var(--white); font-size: 12px; padding: 5px 10px; text-decoration: none; }

  .main-nav { position: absolute; left: 0; top: 72px; width: 1093px; height: 39px; background: var(--blue); }
  .main-nav ul { list-style: none; display: flex; position: absolute; left: 92px; top: 0; height: 39px; align-items: center; gap: 40px; }
  .main-nav a { color: var(--white); font-size: 12px; font-weight: 500; text-decoration: none; letter-spacing: 0.4px; }
  .nav-social { position: absolute; right: 90px; top: 13px; display: flex; gap: 9px; }
  .nav-social span { width: 13px; height: 13px; border-radius: 50%; background: var(--white); }

  .hero { position: absolute; left: 0; top: 111px; width: 1093px; height: 443px;
    background: linear-gradient(120deg, #e9ebf0 0%, #f5f6f9 35%, #e6ebf4 60%, #d9dce4 100%); overflow: hidden; }
  .hero-chart { position: absolute; left: 500px; top: 0; width: 360px; height: 130px;
    background: linear-gradient(180deg, rgba(100,170,225,0.45), rgba(230,236,245,0)); }
  .hero-title { position: absolute; left: 106px; top: 72px; font-size: 40px; font-weight: 500; letter-spacing: 1px; color: var(--ink); z-index: 2; }
  .hero-title .accent { color: var(--orange); }
  .why { position: absolute; left: 124px; top: 133px; z-index: 2; }
  .why h2 { font-size: 19px; font-weight: 500; letter-spacing: 0.5px; margin-bottom: 22px; }
  .why ul { list-style: none; }
  .why li { display: flex; align-items: center; gap: 16px; font-size: 12.3px; height: 28px; }
  .why li svg { flex: none; }
  .hero-person { position: absolute; left: 372px; top: 122px; width: 225px; height: 321px; z-index: 1;
    background: linear-gradient(180deg, #c9a48a 0%, #e8e6e4 30%, #233355 55%, #1c2845 100%); border-radius: 100px 100px 0 0; }

  .join-card { position: absolute; left: 597px; top: 135px; width: 360px; height: 308px; background: var(--white); border: 1px solid #e1e2e5; padding: 20px 17px; z-index: 2; }
  .join-card h3 { font-size: 11.5px; font-weight: 500; letter-spacing: 0.5px; margin-bottom: 14px; }
  .field { display: block; width: 325px; height: 36px; background: var(--field); border: 1px solid var(--field-line); font-family: inherit; font-size: 10.5px; color: #555; padding: 0 9px; margin-bottom: 16px; }
  .btn { display: block; background: var(--orange); color: var(--white); font-family: inherit; font-size: 11.5px; border: none; border-bottom: 2px solid #b84c06; text-align: center; }
  .join-card .btn { width: 126px; height: 36px; margin: 10px 0 0 99px; }
  .join-card .note { margin-top: 34px; font-size: 10px; color: #333; }
  .join-card .note a { color: var(--orange); }

  .offer { position: absolute; left: 0; top: 554px; width: 1093px; height: 453px; }
  .offer-diagram { position: absolute; left: 115px; top: 30px; }
  .offer-copy { position: absolute; left: 599px; top: 64px; width: 395px; }
  .offer-copy h2 { font-size: 23px; font-weight: 500; letter-spacing: 0.8px; }
  .offer-copy .rule { width: 35px; height: 2px; background: var(--ink); margin: 18px 0 34px; }
  .offer-copy p { font-size: 12.3px; line-height: 19.2px; color: var(--grey-text); letter-spacing: 0.55px; }
  .offer-copy .btn { width: 126px; height: 36px; line-height: 34px; margin: 36px 0 0 3px; text-decoration: none; }

  .site-footer { position: absolute; left: 0; top: 1007px; width: 1093px; height: 193px; background: var(--navy); }
  .footer-nav { list-style: none; display: flex; justify-content: center; gap: 41px; position: absolute; top: 38px; width: 100%; }
  .footer-nav a { color: var(--white); font-size: 12.2px; text-decoration: none; }
  .footer-rule { position: absolute; left: 80px; top: 105px; width: 934px; height: 1px; background: #2f3857; }
  .footer-social { position: absolute; left: 494px; top: 92px; display: flex; gap: 14px; }
  .footer-social span { width: 26px; height: 26px; border: 1px solid var(--white); background: var(--navy); }
  .copyright { position: absolute; top: 149px; width: 100%; text-align: center; color: var(--white); font-size: 10px; letter-spacing: 0.3px; }
</style>
</head>
<body>
  <header class="site-header">
    <div class="brand"><span class="brand-dot"></span><span class="brand-name">bramwelloq</span></div>
    <nav class="account-links"><a href="#">Sign in</a><a href="#">Register</a></nav>
  </header>

  <nav class="main-nav">
    <ul>
      <li><a href="#">ABOUT OUR SCHOOL</a></li>
      <li><a href="#">RISK WARNING</a></li>
      <li><a href="#">FAQ</a></li>
      <li><a href="#">TRADING CLOSSARY</a></li>
      <li><a href="#">CONTACT</a></li>
    </ul>
    <div class="nav-social"><span aria-label="Social link"></span><span aria-label="Social link"></span><span aria-label="Social link"></span></div>
  </nav>

  <section class="hero">
    <div class="hero-chart" role="img" aria-label="Blurred background photo of printed bar charts on a desk"></div>
    <h1 class="hero-title"><span class="accent">Take control.</span> Take it easy.</h1>
    <div class="hero-person" role="img" aria-label="Photo of a smiling man in a navy blazer with his hand on his chest"></div>
    <div class="why">
      <h2>Why to join us?</h2>
      <ul>
        <li><svg width="14" height="14" viewBox="0 0 14 14"><circle cx="7" cy="7" r="7" fill="#4285f4"/><path d="M6 4.5 8.5 7 6 9.5" stroke="#fff" stroke-width="1.5" fill="none"/></svg>Best trading tips ever</li>
        <li><svg width="14" height="14" viewBox="0 0 14 14"><circle cx="7" cy="7" r="7" fill="#4285f4"/><path d="M6 4.5 8.5 7 6 9.5" stroke="#fff" stroke-width="1.5" fill="none"/></svg>Secret tips from experts</li>
        <li><svg width="14" height="14" viewBox="0 0 14 14"><circle cx="7" cy="7" r="7" fill="#4285f4"/><path d="M6 4.5 8.5 7 6 9.5" stroke="#fff" stroke-width="1.5" fill="none"/></svg>We teach you how to trade online</li>
        <li><svg width="14" height="14" viewBox="0 0 14 14"><circle cx="7" cy="7" r="7" fill="#4285f4"/><path d="M6 4.5 8.5 7 6 9.5" stroke="#fff" stroke-width="1.5" fill="none"/></svg>Learn how to trade commodities</li>
        <li><svg width="14" height="14" viewBox="0 0 14 14"><circle cx="7" cy="7" r="7" fill="#4285f4"/><path d="M6 4.5 8.5 7 6 9.5" stroke="#fff" stroke-width="1.5" fill="none"/></svg>Learn how to become a trader</li>
      </ul>
    </div>
    <form class="join-card">
      <h3>Join Our School Now!</h3>
      <input class="field" type="text" placeholder="First Name">
      <input class="field" type="text" placeholder="Last Name">
      <input class="field" type="email" placeholder="Email Address">
      <button class="btn" type="submit">Join Now!</button>
      <p class="note">Joined already? <a href="#">Sign In</a></p>
    </form>
  </section>

  <section class="offer">
    <svg class="offer-diagram" width="400" height="400" viewBox="0 0 400 400" font-family="Oswald, sans-serif">
      <circle cx="199" cy="200" r="158" fill="none" stroke="var(--ring)" stroke-width="1.5"/>
      <circle cx="199" cy="195" r="90" fill="var(--navy)"/>
      <g fill="var(--blue)">
        <circle cx="199" cy="38" r="31"/><path d="M193 66 199 74 205 66Z"/>
        <circle cx="359" cy="189" r="31"/><path d="M331 183 323 189 331 195Z"/>
        <circle cx="199" cy="360" r="31"/>
        <circle cx="40" cy="190" r="31"/>
      </g>
      <g fill="#fff" font-size="30" text-anchor="middle" font-weight="500">
        <text x="199" y="49">01</text>
        <text x="359" y="200">02</text>
        <text x="199" y="371">03</text>
        <text x="40" y="201">04</text>
      </g>
      <rect x="75" y="177" width="90" height="33" rx="6" fill="#fff"/>
      <rect x="235" y="177" width="90" height="33" rx="6" fill="#fff"/>
      <g fill="var(--label)" font-size="14" text-anchor="middle" letter-spacing="0.8">
        <text x="202" y="96">HOW TO TRADE ONLINE</text>
        <text x="115" y="199">EXPERT TIPS</text>
        <text x="282" y="200">BE A TRADER</text>
        <text x="204" y="317">TRADE COMMODITIES</text>
      </g>
    </svg>
    <div class="offer-copy">
      <h2>What do we offer?</h2>
      <div class="rule"></div>
      <p>Lorem ipsum dolor sit amet, consectetur adipiscing elit. Integer venenatis, ligula id tincidunt consequat, nisi tellus luctus lectus, a porta nunc quam nec odio. Nulla sagittis sollicitudin tristique. Etiam neque quam, sodales eget feugiat vitae, dictum quis justo. Morbi vitae risus at purus imperdiet faucibus. Fusce dignissim mollis ligula, non congue ante vulputate eget. Morbi aliquet dignissim mauris, vel laoreet mauris tempus sit amet. Quisque mollis nunc et dui dignissim, vitae sagittis quam cursus. Aliquam efficitur rhoncus ex et pulvinar.</p>
      <a class="btn" href="#">Read More</a>
    </div>
  </section>

  <footer class="site-footer">
    <ul class="footer-nav">
      <li><a href="#">HOME</a></li>
      <li><a href="#">ABOUT OUR SCHOOL</a></li>
      <li><a href="#">RISK WARNING</a></li>
      <li><a href="#">FAQ</a></li>
      <li><a href="#">TRADING CLOSSARY</a></li>
      <li><a href="#">CONTACT</a></li>
    </ul>
    <div class="footer-rule"></div>
    <div class="footer-social"><span aria-label="Social link"></span><span aria-label="Social link"></span><span aria-label="Social link"></span></div>
    <p class="copyright">©2016, Bramwelloq Inc. All Rights Reserved.</p>
  </footer>
</body>
</html>
```